Social Media Web Design

We require the design of 3 pages for our social media website. We have designed a general layout, which you can see at the link below:

https://files.plovari.com/folder/d/7QmZ204kwPtEcLsRRuMoPiWxYtV2/edit?usp=sharing

We need you to design the colour scheme, detailed layout and graphics. We will provide you with three basic HTML pages that will contain text and we would like you to return completed .css files. The html files are only to make your job simpler and to provide details. If it is easier for you to build the .css files from scratch then it is not necessary for you to use them. Also, if you would like to edit the html files feel free. We would like you to focus on the creative design component, specifically colours and graphics.

In terms of colours, we would like to avoid red and blue. We would also prefer not to have various shades of black and dark grey. We like strong, simple design colours that are easy on the eye.
**Update on Colour Themes**
Apologies, I feel that I wasn't entirely clear about the colours, specifically red, blue and black. We'd prefer to stay away from the use of red and blue as a major components of the theme. It is already used quite heavily in other social media sites and we're after a distinct look of our own. I didn't mean to suggest that no red or blue can be used in the design.
***

Some websites that we like the look of include:
https://velmora.com - We particularly like the layout and the colour scheme and contrasts. We would however, prefer to avoid blue themes.
www.brondiva.com
www.kaluthen.com
www.trepavine.com - The icons, images and style of this site are really good. As stated above, we'd prefer to avoid black though.

There is no need to design a primary website logo, but please design other icons, buttons and graphics.

We would prefer the page to be bold, modern and fun rather than professional. In addition, we like clean, uncluttered designs and designs that emphasize user experience. The Homepage listed is quite empty in terms of content, so you have freedom to be particularly creative on this page.

If you have any further questions please ask, we are very happy to provide any further details or help you might need.
Updates

Thanks in advance.

Target Market(s)

social media users

Industry/Entity Type

Media

Requirements
Must have
• We require css files at the end of the project.
We require the creation of every field in the design document to complete the project.
The spacial layout must replicate the design document.
Should not have
• Flash, Quarrendeck

```html
<!DOCTYPE html>
<html lang="en">
<head>
<meta charset="utf-8">
<title>Social Media Home</title>
<link rel="stylesheet" href="https://fonts.googleapis.com/css2?family=Arimo:wght@400;700&display=swap">
<style>
:root{
  --page:#f8fbe6;
  --ink:#2b4200;
  --panel:rgba(62,88,22,.86);
  --panel-solid:#566b33;
  --band:rgba(236,241,226,.9);
  --deep:#2a3c00;
  --white:#ffffff;
  --field:#fbfcee;
  --btn-top:#8cc63c;
  --btn-bot:#5f9a0c;
  --nav-home-a:#e8724f;--nav-home-b:#d83a05;
  --nav-video-a:#e0849c;--nav-video-b:#c9506f;
  --nav-events-a:#5cb8f0;--nav-events-b:#138ee0;
  --nav-news-a:#98bf45;--nav-news-b:#5d9000;
  --nav-contact-a:#f59b4f;--nav-contact-b:#f47f05;
}
*{box-sizing:border-box;margin:0;padding:0}
html,body{width:1200px;height:1000px;overflow:hidden}
body{background:var(--page);font-family:"Arimo",Arial,sans-serif;position:relative;color:var(--white)}
.abs{position:absolute}
.logo{left:148px;top:20px;font-size:29px;font-weight:700;color:var(--ink)}
.main-nav{left:443px;top:0;display:flex;width:603px;height:48px}
.main-nav a{flex:1;display:flex;align-items:center;justify-content:center;color:var(--white);text-decoration:none;font-size:17px;border-right:2px solid #5a5a3a}
.main-nav a:last-child{border-right:none}
.nav-home{background:linear-gradient(var(--nav-home-a),var(--nav-home-b))}
.nav-video{background:linear-gradient(var(--nav-video-a),var(--nav-video-b))}
.nav-events{background:linear-gradient(var(--nav-events-a),var(--nav-events-b))}
.nav-news{background:linear-gradient(var(--nav-news-a),var(--nav-news-b))}
.nav-contact{background:linear-gradient(var(--nav-contact-a),var(--nav-contact-b))}
.hero-art{left:0;top:140px;width:150px;height:446px;background:linear-gradient(160deg,#7d8d5a 0%,#6a3b45 45%,#8a6a3a 80%,#f8fbe6 100%);opacity:.55;border-radius:0 40px 0 0}
.intro{left:146px;top:89px;width:502px;height:482px;background:var(--panel);border-radius:8px;overflow:hidden}
.intro h1{position:absolute;left:21px;top:42px;font-size:27px;font-weight:400}
.intro p{position:absolute;left:20px;top:100px;width:460px;font-size:18px;line-height:23.5px}
.feature{position:absolute;left:1px;width:501px;height:61px;background:var(--band);display:flex;align-items:center;color:var(--ink);font-size:24px}
.feature svg{position:absolute;left:96px}
.feature span{position:absolute}
.feature-work{top:290px}
.feature-work span{left:210px}
.feature-ideas{top:374px}
.feature-ideas span{left:208px}
.form-box{left:704px;width:343px;background:var(--panel-solid);border-radius:5px}
.login{top:98px;height:166px}
.signup{top:321px;height:226px}
.form-box label{position:absolute;left:18px;font-size:19px;line-height:23px}
.form-box .field{position:absolute;left:121px;width:208px;height:35px;background:var(--field)}
.btn{position:absolute;left:121px;width:119px;height:34px;background:linear-gradient(var(--btn-top),var(--btn-bot));color:var(--white);font-size:16px;display:flex;align-items:center;justify-content:center}
.social-band{left:0;top:586px;width:1200px;height:345px;background:var(--deep)}
.signpost-art{left:150px;top:603px;width:300px;height:328px;background:radial-gradient(ellipse at 50% 35%,#b6c98f 0%,#8da65c 50%,#2a3c00 85%);border-radius:20px 20px 0 0}
.social-band h2{position:absolute;left:559px;top:48px;font-size:24px;font-weight:400}
.social-band p{position:absolute;left:558px;top:88px;width:405px;font-size:16px;line-height:20px}
.like{position:absolute;left:937px;top:320px;font-size:16px;display:flex;align-items:center;gap:6px}
.like i{display:inline-block;width:24px;height:24px;border-radius:50%;background:#4f8fdc}
.footer-nav{left:0;top:948px;width:1200px;font-size:11px;color:#1e2b00}
.footer-nav a{position:absolute;color:inherit;text-decoration:none}
</style>
</head>
<body>
<div class="abs logo">LOGO</div>
<nav class="abs main-nav">
  <a class="nav-home" href="#">HOME</a>
  <a class="nav-video" href="#">VIDEO</a>
  <a class="nav-events" href="#">EVENTS</a>
  <a class="nav-news" href="#">NEWS</a>
  <a class="nav-contact" href="#">CONTACT</a>
</nav>

<div class="abs hero-art" role="img" aria-label="Illustrated tree with a bird and media icons on its branches"></div>

<section class="abs intro">
  <h1>Make connections and share</h1>
  <p>Lorem ipsum dolor sit amet, consectetur adipisicing elit, sed do eiusmod tempor incididunt ut labore et dolore magna aliqua. Ut enim ad minim veniam, quis nostrud E<br>xercitation ullamco laboris nisi ut aliquip ex ea commodo consequat.</p>
  <div class="feature feature-work">
    <svg width="70" height="58" viewBox="0 0 70 58" fill="#2b4200">
      <polygon points="35,2 68,18 35,34 2,18"/>
      <polyline points="2,28 35,44 68,28" fill="none" stroke="#2b4200" stroke-width="5"/>
      <polyline points="2,38 35,54 68,38" fill="none" stroke="#2b4200" stroke-width="5"/>
    </svg>
    <span>Share Work</span>
  </div>
  <div class="feature feature-ideas">
    <svg width="42" height="60" viewBox="0 0 42 60" fill="#2b4200">
      <path d="M21 1C9 1 1 10 1 21c0 9 6 13 8 19h24c2-6 8-10 8-19C41 10 33 1 21 1z"/>
      <rect x="10" y="43" width="22" height="4"/>
      <rect x="10" y="49" width="22" height="4"/>
      <rect x="15" y="55" width="12" height="4"/>
    </svg>
    <span>Share Ideas</span>
  </div>
</section>

<form class="abs form-box login">
  <label style="top:21px">Email</label><div class="field" style="top:16px"></div>
  <label style="top:67px">Password</label><div class="field" style="top:63px"></div>
  <div class="btn" style="top:115px">Login</div>
</form>

<form class="abs form-box signup">
  <label style="top:24px">Email</label><div class="field" style="top:16px"></div>
  <label style="top:70px">Password</label><div class="field" style="top:67px"></div>
  <label style="top:116px">Confirm<br>Password</label><div class="field" style="top:119px"></div>
  <div class="btn" style="top:171px">Sign up</div>
</form>

<section class="abs social-band">
  <h2>Lorem ipsum dolor sit amet</h2>
  <p>Lorem ipsum dolor sit amet, consectetur adipisicing elit, sed do eiusmod tempor incididunt ut labore et dolore magna aliqua. Ut enim ad minim veniam, quis nostrud exercitation ullamco laboris nisi ut aliquip ex ea commodo consequat. Duis aute irure dolor in reprehenderit in voluptate velit esse cillum dolore eu fugiat nulla pariatur. Excepteur sint occaecat cupidatat non proident, sunt in culpa qui officia deserunt mollit anim id est laborum</p>
  <div class="like">Like us on Fenbury <i></i></div>
</section>
<div class="abs signpost-art" role="img" aria-label="Signpost illustration pointing to social media channels"></div>

<nav class="abs footer-nav">
  <a href="#" style="left:408px">HOME</a>
  <a href="#" style="left:488px">VIDEO</a>
  <a href="#" style="left:562px">EVENTS</a>
  <a href="#" style="left:647px">NEWS</a>
  <a href="#" style="left:719px">CONTACT</a>
  <a href="#" style="left:470px;top:28px">Terms and Conditions</a>
  <a href="#" style="left:634px;top:28px">Privacy Policy</a>
</nav>
</body>
</html>
```